BARRIER BANNER KTV

I am looking for a visual for a banner
3 meters long by 1 high.
In the same theme as the visual identity of the company.
As simple as possible without overloading

There must be the LOGO, the title VOLTARIS SERVICES TECHNIQUES

_________________________

I am looking for a visual for a banner (barrier banner)
3 meters long by 1 high.

AIR CONDITIONING HEATING VENTILATION
04 52 31 69 14

Font styles to use
Sans Serif

Colors
33b8a4
00a990
33a6d7
0493ce
3176b5
0355a3
ffffff

Requirements
Should not have
• No photo
No photo

```html
<!DOCTYPE html>
<html lang="fr">
<head>
<meta charset="utf-8">
<title>KTV – Banderole barrière</title>
<link rel="stylesheet" href="https://fonts.googleapis.com/css2?family=Barlow+Condensed:wght@600;700;800&display=swap">
<style>
  :root {
    --page-bg: #d6d6d6;
    --navy: #22324a;
    --brand-blue: #0a5f86;
    --teal: #2aa59a;
    --deep-teal: #00735f;
    --ocean: #036a93;
    --sky: #1a8ec7;
    --ink: #1c1c1c;
    --white: #ffffff;
  }
  * { margin: 0; padding: 0; box-sizing: border-box; }
  html, body { width: 1111px; height: 1200px; overflow: hidden; background: var(--page-bg); }
  .banner {
    position: absolute; left: 31px; top: 425px; width: 1049px; height: 349px;
    background: linear-gradient(100deg, #e6e6e6 0%, #f4f4f4 40%, var(--white) 70%);
    box-shadow: 0 8px 14px rgba(0,0,0,.25);
    font-family: "Barlow Condensed", sans-serif;
    overflow: hidden;
  }
  .brand-mark {
    position: absolute; left: 20px; top: 12px; width: 410px; height: 220px;
    display: flex; align-items: center; justify-content: center;
  }
  .brand-name {
    font-weight: 800; font-size: 238px; line-height: 220px; letter-spacing: 6px;
    color: var(--navy);
  }
  .title-main {
    position: absolute; left: 473px; top: 22px;
    font-weight: 700; font-size: 100px; line-height: 100px; color: var(--brand-blue);
  }
  .title-band {
    position: absolute; left: 440px; top: 123px; width: 609px; height: 67px;
    background: linear-gradient(90deg, var(--ocean), var(--teal));
    color: var(--white); font-weight: 700; font-size: 56px; line-height: 67px; padding-left: 33px;
    white-space: nowrap;
  }
  .services {
    position: absolute; left: 475px; top: 198px;
    font-weight: 700; font-size: 33px; line-height: 36px; color: var(--ink);
    white-space: nowrap;
  }
  .bands { position: absolute; left: 0; top: 0; width: 1049px; height: 349px; }
  .contact {
    position: absolute; display: flex; align-items: center; color: var(--white); font-weight: 700;
    white-space: nowrap;
  }
  .contact-phone { left: 34px; top: 250px; height: 90px; font-size: 58px; gap: 18px; }
  .contact-web { left: 473px; top: 257px; height: 92px; font-size: 35px; gap: 18px; }
</style>
</head>
<body>
  <section class="banner">
    <svg class="bands" viewBox="0 0 1049 349" aria-hidden="true">
      <defs>
        <linearGradient id="phoneBand" x1="0" x2="1">
          <stop offset="0" stop-color="#22324a"/><stop offset="1" stop-color="#0a4f78"/>
        </linearGradient>
        <linearGradient id="webBand" x1="0" x2="1">
          <stop offset="0" stop-color="#036a93"/><stop offset="1" stop-color="#00735f"/>
        </linearGradient>
      </defs>
      <polygon points="0,237 440,237 462,258 438,303 466,349 0,349" fill="url(#phoneBand)"/>
      <polygon points="468,257 1049,257 1049,349 478,349 452,303" fill="url(#webBand)"/>
    </svg>

    <div class="brand-mark">
      <span class="brand-name">KTV</span>
    </div>

    <div class="title-main">VOLTARIS</div>
    <div class="title-band">SERVICES TECHNIQUES</div>
    <div class="services">AIR CONDITIONING HEATING VENTILATION</div>

    <div class="contact contact-phone">
      <svg width="48" height="48" viewBox="0 0 24 24" aria-hidden="true">
        <path fill="#33b8a4" d="M6.6 10.8a15.1 15.1 0 0 0 6.6 6.6l2.2-2.2a1 1 0 0 1 1-.25 11.4 11.4 0 0 0 3.6.57 1 1 0 0 1 1 1V20a1 1 0 0 1-1 1A17 17 0 0 1 3 4a1 1 0 0 1 1-1h3.5a1 1 0 0 1 1 1c0 1.25.2 2.45.57 3.570a1 1 0 0 1-.25 1z"/>
        <path fill="none" stroke="#33b8a4" stroke-width="1.6" d="M14 6.5a4 4 0 0 1 3.5 3.5M14 2.8a7.6 7.6 0 0 1 7.2 7.2"/>
      </svg>
      <span>04 52 31 69 14</span>
    </div>

    <div class="contact contact-web">
      <svg width="36" height="36" viewBox="0 0 24 24" aria-hidden="true">
        <g fill="none" stroke="#33b8a4" stroke-width="1.6">
          <circle cx="12" cy="12" r="10"/><ellipse cx="12" cy="12" rx="4.5" ry="10"/>
          <path d="M2 12h20M4 6.5h16M4 17.5h16M12 2v20"/>
        </g>
      </svg>
      <span>voltaris-services-techniques.fr</span>
    </div>
  </section>
</body>
</html>
```